We need a wesbite for a new company based in London called: 'Belgrove Maids'. We supply the following services in private household: nanny, housekeeper, maternity nurse, driver, carer, companion and cleaner.
We would like to see designs that should communicate good ethics and high standard, quality services and professionalism.

I want a website something like: www.brightnestnursery.co.uk and http://www.tidyhearthstaff.co.uk/ I want the landing page should have at least 3 seconds intervals of changing photos of Asian (only) particularly Filipino (from the Philippines) Nanny with Children, Asian Housekeeper with apron cleaning, a photo of elderly in a wheelchair with the carer and a picture of a happy family with asian nanny in the background cleaning.

```html
<!DOCTYPE html>
<html lang="en">
<head>
<meta charset="utf-8">
<title>Belgrove Maids – Household Staff London</title>
<link rel="stylesheet" href="https://fonts.googleapis.com/css2?family=Raleway:wght@300;400;600;800&family=Lato:wght@400;700&family=Playfair+Display:wght@400;700&display=swap">
<style>
:root{
  --plum:#a3357a;
  --plum-dark:#862662;
  --plum-deep:#7a1f58;
  --pink-soft:#e7a6cf;
  --gold:#f6c230;
  --gold-dark:#e2a312;
  --amber:#e9ad14;
  --magenta:#c4175d;
  --ink:#333;
  --grey:#666;
  --light:#f1f1f1;
  --white:#fff;
}
*{box-sizing:border-box;margin:0;padding:0}
html,body{width:1200px;height:3046px;overflow:hidden;background:var(--white)}
body{font-family:'Lato',sans-serif;color:var(--ink)}
.page{position:relative;width:1200px;height:3046px;overflow:hidden}
.abs{position:absolute}

/* header */
.site-header{position:absolute;left:0;top:0;width:1200px;height:142px;background:var(--plum)}
.topbar{position:absolute;left:609px;top:0;width:473px;height:45px;background:var(--plum-dark)}
.topbar-call{position:absolute;left:30px;top:6px;display:flex;gap:14px;align-items:center;color:#e9c6dc;font-size:12px;line-height:15px}
.topbar-appt{position:absolute;left:225px;top:0;width:248px;height:45px;background:var(--plum-deep);display:flex;align-items:center;gap:14px;padding-left:20px;color:var(--white);font-family:'Playfair Display',serif;font-size:13px;line-height:15px}
.topbar-appt small{font-size:11px;display:block}
.brand{position:absolute;left:75px;top:58px;color:var(--white);font-family:'Raleway',sans-serif;font-weight:800;line-height:1}
.brand .l1{font-size:25px;letter-spacing:.5px;display:block}
.brand .l2{font-size:40px;letter-spacing:2px;display:block;margin-top:2px}
.main-nav{position:absolute;top:61px;left:603px;display:flex;height:67px;align-items:center;font-family:'Raleway',sans-serif;font-size:15px;color:var(--white)}
.main-nav a{color:inherit;text-decoration:none;position:absolute;white-space:nowrap;transform:translateX(-50%)}
.main-nav .active{background:var(--gold);left:0;transform:none;width:59px;height:67px;display:flex;align-items:center;justify-content:center}

/* hero */
.hero{position:absolute;left:0;top:142px;width:1200px;height:609px;background:linear-gradient(100deg,#e9b9c4 0%,#f4dcd9 40%,#f2e6e0 60%,#fbf8f3 100%)}

/* welcome */
.welcome{position:absolute;left:47px;top:751px;width:1106px;height:447px}
.welcome-text{position:absolute;left:0;top:0;width:562px;height:447px;background:var(--plum);padding:56px 38px 0 38px;color:var(--white)}
.welcome-text .kicker{font-family:'Raleway',sans-serif;font-weight:800;font-size:20px;letter-spacing:.5px}
.welcome-text .name1{font-family:'Raleway',sans-serif;font-weight:800;font-size:38px;margin-top:6px;line-height:1}
.welcome-text .name2{font-family:'Raleway',sans-serif;font-weight:800;font-size:56px;color:var(--pink-soft);line-height:1;margin-top:4px;letter-spacing:1px}
.welcome-text .rule{width:427px;height:2px;background:var(--white);margin-top:8px}
.welcome-text p{font-size:13px;line-height:21px;margin-top:22px;width:440px}
.btn-gold{display:inline-flex;align-items:center;justify-content:center;background:var(--gold);color:var(--white);font-family:'Raleway',sans-serif;font-weight:600;font-size:14px;text-transform:uppercase;border:2px solid #fbe6a6;outline:2px solid var(--gold)}
.welcome-text .btn-gold{position:absolute;left:44px;top:364px;width:141px;height:38px}
.welcome-photo{position:absolute;left:562px;top:0;width:544px;height:447px;background:linear-gradient(135deg,#6d5a55 0%,#9c8c8f 45%,#c99bb6 75%,#e0c7d0 100%)}

/* services */
.services{position:absolute;left:0;top:1198px;width:1200px;height:762px;background:linear-gradient(180deg,#f4f2f2,#ececec 60%,#f3f3f3)}
.services-bg{position:absolute;inset:0;background:radial-gradient(ellipse at 50% 45%,#dedad9 0%,#efeeee 70%)}
.section-title{position:absolute;width:100%;text-align:center;font-family:'Raleway',sans-serif;font-weight:300;font-size:34px;color:#444}
.section-title b{font-weight:600}
.services .section-title{top:74px}
.title-rule{position:absolute;height:2px;background:var(--plum)}
.services-intro{position:absolute;left:165px;top:152px;width:870px;text-align:center;font-size:12px;line-height:22px;color:#555}
.carousel-arrow{position:absolute;top:460px}
.service-card{position:absolute;top:0;width:228px;height:396px}
.service-card .panel{position:absolute;left:0;top:94px;width:228px;height:302px;background:rgba(255,255,255,.9);box-shadow:0 1px 4px rgba(0,0,0,.05)}
.service-card .shape{position:absolute;left:0;top:0}
.service-card h3{position:absolute;top:220px;width:100%;text-align:center;font-family:'Lato',sans-serif;font-weight:700;font-size:16px;color:#222}
.service-card p{position:absolute;top:246px;left:12px;width:204px;font-size:12px;line-height:19px;color:#555;text-align:justify}
.service-card .btn-gold{position:absolute;left:64px;top:361px;width:100px;height:30px;font-size:12px;outline:none;border:none}

/* testimonial */
.testimonial{position:absolute;left:0;top:1960px;width:1200px;height:446px;background:linear-gradient(180deg,#eeb215,#e5a20c 60%,#e7a815)}
.testimonial .section-title{top:52px;color:var(--white);font-family:'Playfair Display',serif;font-weight:400;font-size:30px}
.testimonial .section-title b{font-weight:400;color:#3a2a05}
.quote-badge{position:absolute;left:555px;top:108px;width:90px;height:90px;border-radius:50%;background:var(--white);display:flex;align-items:center;justify-content:center;font-family:'Playfair Display',serif;font-weight:700;font-size:80px;line-height:1;color:#333;padding-top:34px}
.testimonial blockquote{position:absolute;left:120px;top:218px;width:960px;text-align:center;color:var(--white);font-size:15px;line-height:23px}
.testimonial cite{position:absolute;top:328px;width:100%;text-align:center;color:var(--white);font-style:italic;font-weight:700;font-size:16px;letter-spacing:.5px}
.slide-dots{position:absolute;left:477px;top:397px;display:flex;gap:4px}
.slide-dots span{width:52px;height:4px;background:var(--white)}
.slide-dots span.on{background:#222}

/* contact */
.contact{position:absolute;left:0;top:2406px;width:1200px;height:477px;background:#f7f7f7}
.contact h2{position:absolute;left:57px;top:106px;font-family:'Raleway',sans-serif;font-weight:300;font-size:34px;color:#222}
.contact h2 b{font-weight:600}
.contact .lead{position:absolute;left:65px;top:166px;width:490px;font-size:12px;line-height:22px;color:#555}
.info-col{position:absolute;top:276px;width:140px}
.info-col .head{display:flex;align-items:center;gap:12px;font-family:'Raleway',sans-serif;font-weight:600;font-size:17px;color:#222}
.info-col .line{height:3px;background:#e3e3e3;margin-top:12px;width:140px}
.info-col .body{margin-top:16px;font-size:12px;line-height:21px;color:#777}
.appt-form{position:absolute;left:599px;top:56px;width:534px;height:386px;background:var(--white);box-shadow:0 0 8px rgba(0,0,0,.12)}
.appt-form h3{position:absolute;width:100%;top:38px;text-align:center;font-family:'Playfair Display',serif;font-weight:400;font-size:24px;color:#222}
.appt-form h3 b{font-weight:700}
.field{position:absolute;background:var(--light);font-size:13px;color:#888;padding:14px 16px}
.appt-form .note{position:absolute;left:40px;top:327px;font-size:13px;color:#777}
.appt-form .submit{position:absolute;left:280px;top:303px;width:225px;height:44px;background:var(--magenta);color:var(--white);font-size:13px;font-weight:700;display:flex;align-items:center;justify-content:center}

/* footer */
.site-footer{position:absolute;left:0;top:2883px;width:1200px;height:163px;background:var(--plum)}
.social{position:absolute;top:78px;left:476px;display:flex;gap:34px}
.social span{width:30px;height:30px;border-radius:50%;background:#c06a9f}
.copyright{position:absolute;top:128px;width:100%;text-align:center;color:var(--white);font-size:13px}
</style>
</head>
<body>
<div class="page">

  <header class="site-header">
    <div class="topbar">
      <div class="topbar-call">
        <svg width="22" height="22" viewBox="0 0 22 22"><circle cx="11" cy="11" r="9" fill="none" stroke="#e9c6dc" stroke-width="2"/><path d="M6 11l4 4 7-8" fill="none" stroke="#e9c6dc" stroke-width="2"/></svg>
        <span>Call Today 123 456 789<br>Ashford, SC 29001</span>
      </div>
      <div class="topbar-appt">
        <svg width="24" height="24" viewBox="0 0 24 24"><rect x="2" y="4" width="20" height="18" rx="2" fill="var(--white)"/><rect x="4" y="10" width="16" height="10" fill="var(--plum-deep)"/><rect x="6" y="1" width="3" height="6" fill="var(--white)"/><rect x="15" y="1" width="3" height="6" fill="var(--white)"/></svg>
        <span><b>MAKE AN APPOINTMENT</b><small>Connect me today</small></span>
      </div>
    </div>
    <div class="brand"><span class="l1">BELGROVE</span><span class="l2">MAIDS</span></div>
    <nav class="main-nav">
      <a class="active" href="#">Home</a>
      <a href="#" style="left:122px">About Us</a>
      <a href="#" style="left:242px">Services</a>
      <a href="#" style="left:357px">Testimonials</a>
      <a href="#" style="left:485px">Contact Us</a>
    </nav>
  </header>

  <section class="hero" role="img" aria-label="Photo of a smiling Filipino nanny playing with a young girl"></section>

  <section class="welcome">
    <div class="welcome-text">
      <div class="kicker">WELCOME TO</div>
      <div class="name1">BELGROVE</div>
      <div class="name2">MAIDS</div>
      <div class="rule"></div>
      <p>Lorem Ipsum is simply dummy text of the printing and typesetting industry. Lorem Ipsum has been the industry's standard dummy text ever since the 1500s, when an unknown printer took a galley of type and scrambled it to make a type specimen book. It has survived not only five centuries...</p>
      <a class="btn-gold">Know More</a>
    </div>
    <div class="welcome-photo" role="img" aria-label="Photo of an elderly woman in a wheelchair with her smiling carer"></div>
  </section>

  <section class="services">
    <div class="services-bg" role="img" aria-label="Faded background photo of a happy family"></div>
    <h2 class="section-title">Services <b>We Supply</b></h2>
    <div class="title-rule" style="left:456px;top:128px;width:320px"></div>
    <p class="services-intro">It has survived not only five centuries, but also the leap into electronic typesetting, remaining essentially unchanged. It was popularised in the 1960s with the release of printed sheets containing Lorem Ipsum passages, and more recently with desktop publishing software like page layout tools including versions of Lorem Ipsum.</p>

    <svg class="carousel-arrow" style="left:28px" width="20" height="90" viewBox="0 0 20 90"><path d="M18 2L2 45l16 43" fill="none" stroke="#999" stroke-width="2"/></svg>
    <svg class="carousel-arrow" style="left:1152px" width="20" height="90" viewBox="0 0 20 90"><path d="M2 2l16 43L2 88" fill="none" stroke="#999" stroke-width="2"/></svg>

    <div class="abs" style="left:0;top:294px;width:1200px;height:400px">
      <article class="service-card" style="left:97px">
        <div class="panel"></div>
        <svg class="shape" width="228" height="200" viewBox="0 0 228 200">
          <polygon points="114,0 194,80 178,80 114,16 50,80 34,80" fill="var(--plum)"/>
          <polygon points="114,26 188,100 114,174 40,100" fill="#f0d7c8" role="img" aria-label="Photo of a nanny with two toddlers"/>
        </svg>
        <h3>Household Nanny</h3>
        <p>Lorem Ipsum is simply dummy text of the printing and typesetting industry. Lorem Ipsum has been the industry's standard dummy text.</p>
        <a class="btn-gold">View Detail</a>
      </article>
      <article class="service-card" style="left:355px">
        <div class="panel"></div>
        <svg class="shape" width="228" height="200" viewBox="0 0 228 200">
          <polygon points="114,0 194,80 178,80 114,16 50,80 34,80" fill="var(--plum)"/>
          <polygon points="114,26 188,100 114,174 40,100" fill="#c7dbe6" role="img" aria-label="Photo of a housekeeper in a blue uniform"/>
        </svg>
        <h3>Housekeeper</h3>
        <p>Lorem Ipsum is simply dummy text of the printing and typesetting industry. Lorem Ipsum has been the industry's standard dummy text.</p>
        <a class="btn-gold">View Detail</a>
      </article>
      <article class="service-card" style="left:613px">
        <div class="panel"></div>
        <svg class="shape" width="228" height="200" viewBox="0 0 228 200">
          <polygon points="114,0 194,80 178,80 114,16 50,80 34,80" fill="var(--plum)"/>
          <polygon points="114,26 188,100 114,174 40,100" fill="#e9d6d2" role="img" aria-label="Photo of a maternity nurse with an elderly patient"/>
        </svg>
        <h3>Maternity Nurse</h3>
        <p>Lorem Ipsum is simply dummy text of the printing and typesetting industry. Lorem Ipsum has been the industry's standard dummy text.</p>
        <a class="btn-gold">View Detail</a>
      </article>
      <article class="service-card" style="left:873px">
        <div class="panel"></div>
        <svg class="shape" width="228" height="200" viewBox="0 0 228 200">
          <polygon points="114,0 194,80 178,80 114,16 50,80 34,80" fill="var(--plum)"/>
          <polygon points="114,26 188,100 114,174 40,100" fill="#b9cf9f" role="img" aria-label="Photo of a carer with an elderly man outdoors"/>
        </svg>
        <h3>Old Aged Carer</h3>
        <p>Lorem Ipsum is simply dummy text of the printing and typesetting industry. Lorem Ipsum has been the industry's standard dummy text.</p>
        <a class="btn-gold">View Detail</a>
      </article>
    </div>
  </section>

  <section class="testimonial" role="img" aria-label="Amber tinted mosaic of client portrait photos">
    <h2 class="section-title">Recent <b>Testimonial</b></h2>
    <div class="title-rule" style="left:456px;top:90px;width:320px;background:var(--white)"></div>
    <div class="quote-badge">&ldquo;</div>
    <blockquote>It is a long established fact that a reader will be distracted by the readable content of a page when looking at its layout. The point of using Lorem Ipsum is that it has a more-or-less normal distribution of letters, as opposed to using 'Content here, content here', making it look like readable English. Many desktop publishing packages and web page editors now use Lorem Ipsum as their default model text, and a search for lorem ipsum will uncover many web sites still in their infancy.</blockquote>
    <cite>Elena Marsh, London</cite>
    <div class="slide-dots"><span class="on"></span><span></span><span></span><span></span><span></span></div>
  </section>

  <section class="contact">
    <h2>Contact <b>Info</b></h2>
    <p class="lead">It is a long established fact that a reader will be distracted by the readable content of a page when looking at its layout. The point of using Lorem Ipsum is that it has a more-or-less normal distribution of letters, as opposed to using 'Content here,</p>

    <div class="info-col" style="left:71px">
      <div class="head"><svg width="24" height="24" viewBox="0 0 24 24"><path d="M6 2l4 5-2 3c1 3 3 5 6 6l3-2 5 4-3 4C10 22 2 14 2 5z" fill="var(--plum)"/></svg>Phone</div>
      <div class="line"></div>
      <div class="body">Our Contact Phone<br>+123 456 789<br>+123 456 789</div>
    </div>
    <div class="info-col" style="left:240px">
      <div class="head"><svg width="26" height="22" viewBox="0 0 26 22"><rect x="1" y="4" width="24" height="17" fill="var(--plum)"/><path d="M1 4l12 9 12-9" fill="none" stroke="var(--white)" stroke-width="2"/></svg>Email</div>
      <div class="line"></div>
      <div class="body">Our Contact Email<br>care@belgrovemaids.co.uk</div>
    </div>
    <div class="info-col" style="left:412px">
      <div class="head"><svg width="20" height="26" viewBox="0 0 20 26"><path d="M10 1a9 9 0 00-9 9c0 7 9 15 9 15s9-8 9-15a9 9 0 00-9-9z" fill="var(--plum)"/><circle cx="10" cy="10" r="3.5" fill="#f7f7f7"/></svg>Address</div>
      <div class="line"></div>
      <div class="body">Our Office Location<br>#12, Ashcombe Row,<br>London, UK</div>
    </div>

    <form class="appt-form">
      <h3>Make an <b>Appointment</b></h3>
      <div class="field" style="left:30px;top:94px;width:224px;height:48px">Your name</div>
      <div class="field" style="left:30px;top:163px;width:224px;height:48px">Your email</div>
      <div class="field" style="left:30px;top:232px;width:224px;height:48px">Your subject</div>
      <div class="field" style="left:280px;top:94px;width:225px;height:186px">Your message</div>
      <div class="note">All fields are obligatory</div>
      <div class="submit">Make an Appointment</div>
    </form>
  </section>

  <footer class="site-footer">
    <svg class="abs" style="left:579px;top:0" width="60" height="24" viewBox="0 0 60 24"><path d="M0 0h60c-12 0-18 18-30 18S12 0 0 0z" fill="#f7f7f7"/></svg>
    <div class="social"><span></span><span></span><span></span><span></span><span></span></div>
    <div class="copyright">© Belgrove Maids, Privacy Policy | Terms &amp; Conditions</div>
  </footer>

</div>
</body>
</html>
```